business card for training & coaching company, Brightwell.co

Create a warm, clean, professional 2-sided business card for Brightwell.co.
Brightwell.co is a new company that shares Brightwell Dialogue (combination of mindfulness, kindness, and nonviolent communication), training and coaching individuals and groups.
Include the logo provided, perhaps incorporating a second opaque version of it as well.
Feelings & Needs lists on the reverse side of the card.

Target Market(s)

Women 30-60 years old, university educated.
Spiritual, may be Buddhist.

Industry/Entity Type

Training

Contact Information for Business Card

Marisabel T. Oberholt, MSc
Group Facilitator & Certified Wellness Coach
Brightwell Dialogue training & support
Group Facilitator & Coach
01632 960 418
07700 900 862
www.brightwell-example.co

Font styles to use
Sans Serif

Requirements
Must have
• Front -- Contact details, logo provided.
• Back -- Feelings list; Needs list
• Professional yet warm, inviting, friendly feel.
Nice to have
• little graphics (telephone for phone number, envelope for email, globe for web);
• Clean font (like Sathu, Frutiga, Helvetica).
• Feeling of movement or transformation.
Should not have
• More than 3 colours.
• Loud or busy designs.
• A gentle curve or two is ok, but not swirly designs.
• No black or other heavy backgrounds.

```html
<!DOCTYPE html>
<html lang="en">
<head>
<meta charset="utf-8">
<title>Brightwell.co business card</title>
<link href="https://fonts.googleapis.com/css2?family=Source+Sans+3:wght@400;600;700&family=Arimo:wght@700&display=swap" rel="stylesheet">
<style>
  :root {
    --orange: #f7941d;
    --orange-deep: #f15a24;
    --orange-soft: #f5894f;
    --white: #ffffff;
    --edge: #cfcfcf;
    --page: #ffffff;
  }
  html, body {
    margin: 0;
    padding: 0;
    width: 1200px;
    height: 993px;
    overflow: hidden;
    background: var(--page);
    font-family: "Source Sans 3", sans-serif;
  }
  .card {
    position: absolute;
    left: 225px;
    width: 763px;
    height: 470px;
    border: 2px solid var(--edge);
    box-sizing: content-box;
    background: var(--white);
    overflow: hidden;
  }
  .card--front { top: 25px; }
  .card--back { top: 506px; }
  .card__art {
    position: absolute;
    left: 0; top: 0;
    width: 763px; height: 470px;
  }
  .brand {
    position: absolute;
    left: 24px; top: 44px;
    display: flex;
    align-items: center;
    gap: 14px;
    color: var(--orange);
    font-weight: 700;
    font-size: 42px;
    line-height: 1;
  }
  .brand__dot {
    width: 34px; height: 34px;
    border-radius: 50%;
    background: var(--orange);
  }
  .holder {
    position: absolute;
    left: 80px; top: 163px;
    color: var(--orange);
  }
  .holder__name {
    margin: 0 0 6px;
    font-family: "Arimo", sans-serif;
    font-weight: 700;
    font-size: 27px;
    line-height: 1.1;
  }
  .holder__line {
    margin: 0;
    font-size: 23px;
    line-height: 23px;
  }
  .contact {
    position: absolute;
    left: 133px; top: 329px;
    margin: 0; padding: 0;
    list-style: none;
    color: var(--white);
    font-size: 25px;
    line-height: 27px;
  }
  .contact__item { display: flex; align-items: center; gap: 6px; }
  .contact__icon { width: 26px; height: 22px; flex: none; }
  .lists {
    position: absolute;
    left: 45px;
    display: flex;
    flex-direction: column;
  }
  .lists--needs { top: 26px; color: var(--orange); }
  .lists--feelings { top: 256px; color: var(--white); }
  .lists__title {
    margin: 0 0 20px;
    font-weight: 400;
    font-size: 26px;
    line-height: 28px;
  }
  .lists__cols { display: flex; gap: 0; }
  .lists__col {
    margin: 0; padding: 0;
    list-style: none;
    width: 206px;
    font-size: 27px;
    line-height: 23px;
  }
  .website {
    position: absolute;
    right: 26px; bottom: 24px;
    color: var(--white);
    font-size: 24px;
  }
</style>
</head>
<body>

<section class="card card--front" aria-label="Front of card">
  <svg class="card__art" viewBox="0 0 763 470" aria-hidden="true">
    <defs>
      <linearGradient id="bandFront" x1="0" y1="1" x2="1" y2="0">
        <stop offset="0" stop-color="#f15a24"/>
        <stop offset="0.5" stop-color="#f5894f"/>
        <stop offset="1" stop-color="#f7941d"/>
      </linearGradient>
      <linearGradient id="markFront" x1="0" y1="0" x2="0" y2="1">
        <stop offset="0" stop-color="#f7941d"/>
        <stop offset="0.5" stop-color="#f5894f"/>
        <stop offset="1" stop-color="#f15a24"/>
      </linearGradient>
    </defs>
    <path d="M0,284 C160,274 330,292 530,304 L540,324 C340,314 160,300 0,300 Z" fill="url(#bandFront)"/>
    <path d="M0,318 C180,306 360,328 545,330 C575,385 615,425 672,470 L0,470 Z" fill="url(#bandFront)"/>
    <circle cx="645" cy="315" r="95" fill="url(#markFront)" role="img" aria-label="Large soft brand circle"/>
  </svg>

  <div class="brand"><span class="brand__dot"></span>Brightwell.co</div>

  <div class="holder">
    <p class="holder__name">Marisabel T. Oberholt</p>
    <p class="holder__line">MSc, CWC, CSMCOSCA</p>
    <p class="holder__line">Group Facilitator &amp; Coach</p>
    <p class="holder__line">Brightwell Dialogue training &amp; support</p>
  </div>

  <ul class="contact">
    <li class="contact__item">
      <svg class="contact__icon" viewBox="0 0 26 22" aria-hidden="true"><path d="M3,3 L8,2 L10,7 L7,9 C9,13 12,16 16,18 L18,15 L23,17 L22,21 C12,21 3,13 3,3 Z" fill="#fff"/></svg>
      01632 960 418
    </li>
    <li class="contact__item">
      <svg class="contact__icon" viewBox="0 0 26 22" aria-hidden="true"><rect x="8" y="1" width="10" height="20" rx="2" fill="none" stroke="#fff" stroke-width="2"/><rect x="10" y="4" width="6" height="9" fill="#fff"/></svg>
      07700 900 862
    </li>
    <li class="contact__item">
      <svg class="contact__icon" viewBox="0 0 26 22" aria-hidden="true"><rect x="2" y="5" width="22" height="14" rx="2" fill="none" stroke="#fff" stroke-width="2"/><path d="M3,6 L13,13 L23,6" fill="none" stroke="#fff" stroke-width="2"/></svg>
      marisabel@brightwell-example.co
    </li>
  </ul>
</section>

<section class="card card--back" aria-label="Back of card">
  <svg class="card__art" viewBox="0 0 763 470" aria-hidden="true">
    <defs>
      <linearGradient id="bandBack" x1="0" y1="1" x2="1" y2="0">
        <stop offset="0" stop-color="#f15a24"/>
        <stop offset="0.55" stop-color="#f5894f"/>
        <stop offset="1" stop-color="#f7941d"/>
      </linearGradient>
      <linearGradient id="markBack" x1="0" y1="0" x2="0" y2="1">
        <stop offset="0" stop-color="#f7941d"/>
        <stop offset="1" stop-color="#f15a24"/>
      </linearGradient>
    </defs>
    <path d="M0,224 C250,214 520,252 763,254 L763,264 C520,264 250,240 0,240 Z" fill="url(#bandBack)"/>
    <path d="M0,256 C260,244 520,278 763,280 L763,470 L0,470 Z" fill="url(#bandBack)"/>
    <circle cx="610" cy="176" r="66" fill="url(#markBack)" role="img" aria-label="Soft brand circle"/>
    <ellipse cx="536" cy="318" rx="72" ry="50" fill="#ffffff" role="img" aria-label="Butterfly illustration"/>
  </svg>

  <div class="lists lists--needs">
    <h2 class="lists__title">Needs</h2>
    <div class="lists__cols">
      <ul class="lists__col">
        <li>belonging</li><li>choice</li><li>clarity</li><li>empathy</li><li>freedom</li><li>meaning</li>
      </ul>
      <ul class="lists__col">
        <li>mourning</li><li>peace</li><li>safety</li><li>support</li><li>understanding</li><li>&amp; more...</li>
      </ul>
    </div>
  </div>

  <div class="lists lists--feelings">
    <h2 class="lists__title">Feelings</h2>
    <div class="lists__cols">
      <ul class="lists__col">
        <li>confusion</li><li>curious</li><li>despair</li><li>edgy</li><li>fiery</li><li>grief</li>
      </ul>
      <ul class="lists__col">
        <li>nervous</li><li>powerless</li><li>shock</li><li>torn</li><li>weary</li><li>&amp; more....</li>
      </ul>
    </div>
  </div>

  <p class="website">www.brightwell-example.co</p>
</section>

</body>
</html>
```